Cleaning services Business Card Design

I need a business card design for my Cleaning business. I would like perhaps emphasis on the company name, Muddle to Marvel. Maybe the Muddle would to dirty and the marvel would have sprinkles.

Industry/Entity Type

Business

Contact Information for Business Card

Muddle to Marvel Cleaning Services, Tomas Ordell, Industrial, Commercial, & Residential 415-806-2147

```html
<!DOCTYPE html>
<html lang="en">
<head>
<meta charset="utf-8">
<title>Muddle to Marvel Cleaning Services – Business Card</title>
<link rel="stylesheet" href="https://fonts.googleapis.com/css2?family=Open+Sans:wght@400;600;700&display=swap">
<style>
  :root {
    --backdrop: #e6e8ea;
    --card: #fbfcfc;
    --card-edge: #c9ced2;
    --teal: #1f9aa8;
    --navy: #1c2a3a;
  }
  * { margin: 0; padding: 0; box-sizing: border-box; }
  html, body {
    width: 1200px;
    height: 970px;
    overflow: hidden;
    background: var(--backdrop);
    font-family: "Open Sans", Arial, sans-serif;
  }
  .business-card {
    position: absolute;
    left: 100px;
    top: 207px;
    width: 1000px;
    height: 556px;
    background: var(--card);
    border: 1px solid var(--card-edge);
    box-shadow: 0 10px 30px rgba(0, 0, 0, 0.12);
  }
  .brand {
    position: absolute;
    left: 0;
    right: 0;
    top: 120px;
    text-align: center;
    color: var(--teal);
    font-weight: 700;
  }
  .brand-name {
    font-size: 74px;
    line-height: 1;
    letter-spacing: 1px;
  }
  .brand-tagline {
    margin-top: 22px;
    font-size: 30px;
    letter-spacing: 8px;
    text-transform: uppercase;
  }
  .contact {
    position: absolute;
    left: 0;
    right: 0;
    top: 350px;
    text-align: center;
    color: var(--navy);
  }
  .contact-name {
    color: var(--teal);
    font-size: 38px;
    font-weight: 700;
    line-height: 1.2;
  }
  .contact-phone {
    margin-top: 14px;
    font-size: 26px;
    display: flex;
    justify-content: center;
    align-items: center;
    gap: 10px;
  }
  .contact-phone .label { font-weight: 700; }
  .contact-phone .phone-icon { width: 24px; height: 24px; fill: var(--navy); }
  .services {
    position: absolute;
    left: 0;
    right: 0;
    top: 480px;
    text-align: center;
    color: var(--navy);
    font-size: 24px;
    word-spacing: 4px;
  }
</style>
</head>
<body>
  <div class="business-card">
    <div class="brand">
      <div class="brand-name">Muddle to Marvel</div>
      <div class="brand-tagline">Cleaning Services</div>
    </div>

    <div class="contact">
      <div class="contact-name">Tomas Ordell</div>
      <div class="contact-phone">
        <span class="label">Call us</span>
        <svg class="phone-icon" viewBox="0 0 24 24" aria-hidden="true">
          <path d="M20 15.5c-1.2 0-2.4-.2-3.6-.6-.3-.1-.7 0-1 .2l-2.2 2.2c-2.8-1.4-5.1-3.8-6.6-6.6l2.2-2.2c.3-.3.4-.7.2-1C8.7 6.4 8.5 5.2 8.5 4c0-.6-.4-1-1-1H4c-.6 0-1 .4-1 1 0 9.4 7.6 17 17 17 .6 0 1-.4 1-1v-3.5c0-.6-.4-1-1-1z"/>
        </svg>
        <span class="number">415-806-2147</span>
      </div>
    </div>

    <div class="services">Industrial &nbsp;-&nbsp; Commercial &nbsp;-&nbsp; Residential</div>
  </div>
</body>
</html>
```